AVOID HOT “HARISSA” SAUCE. IN CAN

Brand Overview: Create a dynamic and eye-catching label for our new hot sauce IN CAN, “DUMEL.” Our brand is all about delivering a fiery flavor experience that combines the intensity of various peppers with unique, bold ingredients. The hot sauce targets spice enthusiasts who crave both heat and distinctive taste profiles.

Key Messages: Intensity: Emphasize the extreme heat level of the hot sauce to appeal to spice lovers.
Traditional: The taste is traditional
Flavor Fusion: Highlight the unique blend of peppers and special ingredients that sets DUMEL

Quality Ingredients: Convey the use of premium, natural ingredients to reinforce the high-quality aspect of our product.

Versatility: Communicate the sauce's versatility – perfect for various cuisines and dishes. Design Elements:

Color Palette: Use fiery reds, oranges, and yellows to convey the heat, with accents of dark and smoky tones to suggest depth of flavor.

Typography: Choose bold and legible fonts for the product name, ensuring it is easily readable from a distance.
Imagery: Incorporate visuals of flaming peppers or a stylized fire to reinforce the spicy nature of the hot sauce.
Consider using images of the key ingredients to showcase the fusion of flavors.

Texture/Background: Add a textured or gradient background to enhance visual interest and give a sense of depth.

Label Information: Product Name Hot Sauce "HARISSA" Heat Level

Indicator: Use a visual scale or iconography to indicate the spiciness level.

Ingredients: Highlight key ingredients and emphasize their quality, peppers, water, salt
SIZE: L: 12cm H: 5.5cm

Net Weight: 140g

Regulatory Information: Ensure compliance with all relevant food labeling regulations, including ingredients list, nutritional information, and contact details.

Competitor Analysis: Examine other hot sauce labels in the market to identify design trends and differentiators.
Inspiration: Consider drawing inspiration from elements like flames, peppers, or global spice motifs to create a visually striking and memorable label. Mood/Emotion: The label should evoke excitement, daring, and a sense of adventure – capturing the thrill of experiencing the intense flavor of HARISSA DUMEL Hot Sauce.

Target Audience: Spice enthusiasts, foodies, and individuals seeking a unique and bold addition to their culinary experiences.

Delivery Format: The label design should be suitable for various packaging sizes, ensuring scalability without sacrificing visual impact. Remember to balance the vibrant and intense visuals with clarity and readability and send the FONT at the moment of the delivery.
Updates

Need extra days to review

Target Market(s)

European

Font styles to use
Decorative

Colors
FFF300
FFF600
FEFA6F
FFFEC7
FFFEE8
FFC000
F8CF3A
FAE287
FDF2CF
FEFAEE
EE7325
F08F49
F5BC92
FAE3D3
FDF4ED
EB3D1F
EC4F4E
F09395
F8D3D4
FCEDEE

Requirements
Must have
• LOGO, BARCODE, Nutritional facts, INGREDIENTS

```html
<!DOCTYPE html>
<html lang="en">
<head>
<meta charset="utf-8">
<title>DUMEL Hot Sauce Harissa – Can Label</title>
<link rel="stylesheet" href="https://fonts.googleapis.com/css2?family=Ultra&family=Sniglet:wght@800&family=Poppins:wght@400;600&display=swap">
<style>
  :root {
    --stage: #e9e9ea;
    --label-yellow: #f3c327;
    --label-yellow-deep: #e9b51b;
    --ink: #111111;
    --brand-navy: #1c2560;
    --sauce-red: #d9141c;
    --flame-orange: #ee7325;
    --flame-yellow: #ffc000;
    --pepper-red: #c9151b;
  }
  * { margin: 0; padding: 0; box-sizing: border-box; }
  html, body {
    width: 1200px;
    height: 1198px;
    overflow: hidden;
    background: var(--stage);
  }
  .canvas {
    position: relative;
    width: 1200px;
    height: 1198px;
  }
  .label {
    position: absolute;
    left: 310px;
    top: 99px;
    width: 580px;
    height: 1000px;
    overflow: hidden;
    background: radial-gradient(ellipse at 50% 40%, var(--label-yellow) 0%, var(--label-yellow-deep) 100%);
  }
  .brand-name {
    position: absolute;
    top: 140px;
    left: 0;
    width: 100%;
    text-align: center;
    font-family: "Poppins", sans-serif;
    font-weight: 600;
    font-size: 72px;
    letter-spacing: 2px;
    color: var(--brand-navy);
    line-height: 1;
  }
  .product-line {
    position: absolute;
    left: 0;
    width: 100%;
    text-align: center;
    font-family: "Sniglet", sans-serif;
    font-weight: 800;
    color: var(--ink);
    line-height: 1;
  }
  .product-line--top { top: 300px; font-size: 76px; }
  .product-line--bottom { top: 520px; font-size: 70px; }
  .product-name {
    position: absolute;
    top: 390px;
    left: -40px;
    width: 660px;
    text-align: center;
    font-family: "Ultra", serif;
    font-size: 112px;
    line-height: 1;
    color: var(--sauce-red);
    text-shadow: 6px 6px 0 var(--ink);
    letter-spacing: -1px;
  }
  .heat-illustration {
    position: absolute;
    top: 620px;
    left: 95px;
    width: 390px;
    height: 260px;
  }
  .net-weight {
    position: absolute;
    top: 905px;
    left: 0;
    width: 100%;
    text-align: center;
    font-family: "Poppins", sans-serif;
    font-weight: 400;
    font-size: 26px;
    color: var(--ink);
  }
</style>
</head>
<body>
  <main class="canvas">
    <section class="label">
      <div class="brand-name">DUMEL</div>
      <div class="product-line product-line--top">Hot Sauce</div>
      <h1 class="product-name">HARISSA</h1>
      <div class="product-line product-line--bottom">Heat Level</div>
      <svg class="heat-illustration" viewBox="0 0 390 260" role="img" aria-label="Illustration of a red chili pepper engulfed in flames">
        <defs>
          <radialGradient id="heat-fill" cx="50%" cy="60%" r="60%">
            <stop offset="0%" stop-color="#ffc000"/>
            <stop offset="55%" stop-color="#ee7325"/>
            <stop offset="100%" stop-color="#c9151b"/>
          </radialGradient>
        </defs>
        <rect x="0" y="0" width="390" height="260" rx="40" fill="url(#heat-fill)"/>
      </svg>
      <div class="net-weight">Net Weight: 140g</div>
    </section>
  </main>
</body>
</html>
```